Website for a company focused on genealogical products and historical items

I need a website designed using our current branding.

Company name: R. L. Atelier: Merchants of Fine Heritage Prints

Our company sells ancestral art, downloadable worksheets pertaining to genealogy, and we offer weekend workshops and seminars.

the website should have the following pages:
landing page
products page: to include three different products: 1. a physical product with an intake form the customer completes online, 2. a downloadable product, and 3. a lecture/presentation booking page
about us page/history
contact page/sign up page

The website will include portraits of historical figures in gold frames, lots of white background, very clean design. We would like the website to feel fresh and clean, bright.

Target Market(s)

Older Americans interested in their family heritage and lineage

Industry/Entity Type

Genealogy, research, history, lectures

Coding

Coded - Design and coding required

Number of Pages Required

5+ page

Font styles to use
Serif
Other font styles liked:
• Libre Baskerville, Aliey, one historical script - P22 Royalist

Colors
0094D4
00A9DD
6FCCEA
C7EBF8
E9F6FB

Requirements
Must have
• must have our color branding and logo (pdf attached, and I can send original files), simple design, not too many images on each page (maybe one image per page)
Nice to have
• Nice to have clean design, all pages the same "look"
Should not have
• no black backgrounds, nothing too busy

```html
<!DOCTYPE html>
<html lang="en">
<head>
<meta charset="utf-8">
<title>R. L. Atelier</title>
<link href="https://fonts.googleapis.com/css2?family=Libre+Baskerville:wght@400;700&display=swap" rel="stylesheet">
<style>
:root{
  --blue-deep:#0094d4;
  --blue:#00a9dd;
  --blue-soft:#6fccea;
  --blue-pale:#c7ebf8;
  --blue-mist:#e9f6fb;
  --ink:#1f3a4a;
  --muted:#4a6372;
  --white:#ffffff;
  --field:#8fb9cc;
}
*{box-sizing:border-box;margin:0;padding:0}
html,body{width:1200px;height:2196px;overflow:hidden;background:var(--white)}
body{font-family:'Libre Baskerville',serif;color:var(--ink);position:relative}
.abs{position:absolute}

.site-header{left:0;top:0;width:1200px;height:90px;background:var(--white);border-bottom:1px solid var(--blue-pale)}
.brand{left:448px;top:18px;font-size:14px;color:var(--muted)}
.nav{left:0;width:1200px;top:44px;text-align:center;font-weight:700;font-size:17px}
.nav a{color:var(--ink);text-decoration:none;margin:0 9px}

.hero{left:0;top:90px;width:1200px;height:564px;background:linear-gradient(180deg,var(--blue-deep),var(--blue));color:var(--white);text-align:center;padding-top:138px}
.hero h1{font-size:48px;font-weight:700;line-height:1.1}
.hero p{width:620px;margin:34px auto 0;font-size:23px;line-height:40px}
.btn{display:inline-block;background:var(--blue);color:var(--white);border-radius:4px;font-size:14px;text-align:center;text-decoration:none}
.hero .btn{margin-top:22px;width:184px;height:46px;line-height:46px;background:var(--white);color:var(--blue-deep)}

.products-title{left:57px;top:664px;font-size:34px;font-weight:700}
.card{background:var(--blue-mist);border:1px solid var(--blue-pale);border-radius:6px;width:343px;text-align:center;padding:18px 0 20px}
.card .img-label{font-size:14px;color:var(--muted);height:24px}
.card h3{font-size:21px;font-weight:700;margin-top:18px;line-height:28px}
.card p{font-size:13.5px;line-height:23px;margin:8px 18px 0;color:var(--muted)}
.card .btn{margin-top:16px;height:42px;line-height:42px;padding:0 19px}

.section{left:56px;width:1088px;text-align:center}
.section h2{font-size:34px;font-weight:700;line-height:1.2}
.about p{margin-top:30px;font-size:16.5px;line-height:32px;color:var(--muted)}
.about .link{margin-top:4px;font-size:14px}
.about a{color:var(--blue-deep)}

.contact .lead{margin-top:26px;font-size:14px;color:var(--muted)}
.form{margin-top:14px;font-size:14px;color:var(--muted)}
.form label{margin-left:4px}
.field{display:inline-block;width:162px;height:20px;border:1px solid var(--field);vertical-align:middle;background:var(--white)}
.area{display:inline-block;width:156px;height:58px;border:1px solid var(--field);vertical-align:bottom;background:var(--white)}
.send{display:inline-block;font-size:12px;border:1px solid var(--blue);background:var(--blue);color:var(--white);padding:2px 6px;vertical-align:bottom;margin-left:4px;border-radius:3px}
.info{margin-top:10px;font-size:14px;line-height:25px;color:var(--muted)}
.footer{left:57px;top:2164px;font-size:13px;color:var(--muted)}
</style>
</head>
<body>
<header class="abs site-header">
  <div class="abs brand">R. L. Atelier</div>
  <nav class="abs nav"><a href="#">Products</a> <a href="#">About Us</a> <a href="#">Contact</a></nav>
</header>

<section class="abs hero">
  <h1>Welcome to R. L. Atelier</h1>
  <p>Merchants of Fine Heritage Prints<br>Explore your family heritage through our meticulously crafted ancestral art pieces and educational resources.</p>
  <a class="btn" href="#">Explore Products</a>
</section>

<h2 class="abs products-title">Our Products</h2>

<article class="abs card" style="left:388px;top:654px">
  <div class="img-label">Product 1</div>
  <h3>Physical Product</h3>
  <p>Discover our exquisite collection of physical ancestral art pieces. Each piece is crafted with attention to detail and historical accuracy.</p>
  <a class="btn" href="#">Order Now</a>
</article>
<article class="abs card" style="left:801px;top:654px">
  <div class="img-label">Product 2</div>
  <h3>Downloadable Products</h3>
  <p>Enhance your genealogical research with our downloadable worksheets and templates. Perfect for organizing and documenting your family history.</p>
  <a class="btn" href="#">Download Now</a>
</article>
<article class="abs card" style="left:56px;top:956px">
  <div class="img-label">Product 3</div>
  <h3>Lectures &amp; Presentations</h3>
  <p>Join our educational workshops and seminars led by expert historians. Learn about genealogical research methods and historical insights.</p>
  <a class="btn" href="#">Book a Session</a>
</article>

<section class="abs section about" style="top:1412px">
  <h2>About Us</h2>
  <p>R. L. Atelier: Merchants of Fine Heritage Prints is dedicated to preserving and celebrating family heritage through art and education. Our mission is to provide individuals with the tools and knowledge to explore their roots and connect with their past.<br>Founded in [year], our team of passionate historians and artists bring years of experience in genealogical research and artistic craftsmanship. We believe that understanding one's heritage enriches lives and fosters a deeper appreciation for cultural diversity.</p>
  <p class="link"><a href="#">Contact Us</a></p>
</section>

<section class="abs section contact" style="top:1862px">
  <h2>Contact Us</h2>
  <p class="lead">Have questions or want to learn more about our products and workshops? Feel free to reach out to us!</p>
  <div class="form">
    <label>Name:</label> <span class="field"></span>
    <label>Email:</label> <span class="field"></span>
    <label>Message:</label> <span class="area"></span><span class="send">Send Message</span>
  </div>
  <p class="info">Email: hello@rlatelier-prints.com<br>Phone: +1 (555) 014-2368<br>Follow us on social media:</p>
</section>

<footer class="abs footer">© 2024 R. L. Atelier. All rights reserved.</footer>
</body>
</html>
```